BrightArc Orthodontics Exterior Signage

We need 4 exterior signs designed for our orthodontics practice based in Sydney, Australia. The signs face busy streets and walkways and experience heavy foot traffic. The existing signage has been in use for about 5 years and is starting to feel outdated. We want the signs to be clean and modern with effective use of brand colours and imagery. For details about the practice and brand style, see: brightarcorthodontics.example.au

Target Market(s)

Foot traffic in affluent suburb of Sydney, Australia.

Industry/Entity Type

Health Care

Font styles to use
Sans Serif

Colors

Designer to choose colors to be used in the design.

Requirements
Must have
• Modern, clean, professional feel. Family friendly.
Nice to have
• Effective use of lifestyle imagery. For similar examples, see: https://www.clearvellatrays.example.au
Should not have
• No close-up imagery of teeth or mouths.

```html
<!DOCTYPE html>
<html lang="en">
<head>
<meta charset="utf-8">
<title>BrightArc Orthodontics – Entrance Sign</title>
<link rel="stylesheet" href="https://fonts.googleapis.com/css2?family=Questrial&family=Cabin:wght@500&display=swap">
<style>
  :root {
    --page-bg: #e4e7ea;
    --sign-bg: #eceeed;
    --brand-green: #2a8a6e;
    --band-green: #2b7c67;
    --entry-cyan: #6fe0ee;
    --entry-cyan-soft: #78e3f0;
    --white: #ffffff;
  }
  html, body {
    margin: 0;
    width: 1200px;
    height: 923px;
    overflow: hidden;
    background: var(--page-bg);
  }
  .sign {
    position: absolute;
    left: 436px;
    top: 31px;
    width: 328px;
    height: 860px;
    background: var(--sign-bg);
    overflow: hidden;
    box-shadow: 0 2px 10px rgba(0,0,0,0.12);
  }
  .brand-name {
    position: absolute;
    top: 52px;
    left: 0;
    width: 100%;
    text-align: center;
    font-family: "Questrial", sans-serif;
    font-size: 15px;
    color: var(--brand-green);
    letter-spacing: 0.2px;
    z-index: 2;
  }
  .brand-name .mark {
    display: inline-block;
    width: 10px;
    height: 10px;
    background: var(--brand-green);
    margin-right: 6px;
    vertical-align: 0;
  }
  .headline {
    position: absolute;
    top: 78px;
    right: 6px;
    margin: 0;
    text-align: right;
    font-family: "Questrial", sans-serif;
    font-weight: 400;
    font-size: 40px;
    line-height: 45px;
    color: var(--brand-green);
    z-index: 2;
  }
  .family-photo {
    position: absolute;
    top: 200px;
    left: 0;
    width: 100%;
    height: 247px;
    background:
      radial-gradient(ellipse at 30% 70%, rgba(226,90,140,0.55), transparent 45%),
      radial-gradient(ellipse at 60% 65%, rgba(110,170,175,0.55), transparent 50%),
      linear-gradient(180deg, var(--sign-bg) 0%, #d9c3b2 35%, #c8a48d 70%, #b9b7b3 100%);
    z-index: 1;
  }
  .entrance-band {
    position: absolute;
    top: 447px;
    left: 0;
    width: 100%;
    height: 63px;
    background: var(--band-green);
    display: flex;
    align-items: center;
    justify-content: center;
    font-family: "Cabin", sans-serif;
    font-weight: 500;
    font-size: 50px;
    letter-spacing: 1px;
    color: var(--white);
    z-index: 2;
  }
  .entry-panel {
    position: absolute;
    top: 510px;
    left: 0;
    width: 100%;
    height: 350px;
    background: linear-gradient(160deg, var(--entry-cyan) 0%, var(--entry-cyan-soft) 100%);
  }
  .entry-panel svg {
    position: absolute;
    inset: 0;
  }
</style>
</head>
<body>
  <div class="sign">
    <div class="brand-name"><span class="mark"></span>BrightArc Orthodontics</div>
    <h1 class="headline">Creating<br>great, straight<br>smiles</h1>
    <div class="family-photo" role="img" aria-label="Smiling family of four – father, mother, daughter and son – huddled together"></div>
    <div class="entrance-band">ENTRANCE</div>
    <div class="entry-panel">
      <svg width="328" height="350" viewBox="0 0 328 350" aria-hidden="true">
        <polygon class="divider" points="0,0 328,0 328,3 0,8" fill="#ffffff"/>
        <g fill="var(--brand-green)">
          <polygon class="chevron" points="96,18 126,18 150,47 126,76 96,76 120,47"/>
          <polygon class="chevron" points="139,18 169,18 193,47 169,76 139,76 163,47"/>
          <polygon class="chevron" points="182,18 212,18 236,47 212,76 182,76 206,47"/>
        </g>
      </svg>
    </div>
  </div>
</body>
</html>
```